Letterhead and Envelope Design for Investment Company

We need a letterhead and envelope design.
We are a family owned investment company doing direct investments into other family owned businesses.
I have attached all our current marketing material including our logo for reference.

Our under construction website can be found here:
https://rob-darke-qv7m.pagevorlo.com/
password: Copperfen

Target Market(s)

Bankers, business owners, financial partners

Industry/Entity Type

Investment

Colors

Designer to choose colors to be used in the design.

Requirements
Must have
• Logo, and company information

```html
<!DOCTYPE html>
<html lang="en">
<head>
<meta charset="utf-8">
<title>Copperfen Holdings – Letterhead and Envelope</title>
<link rel="stylesheet" href="https://fonts.googleapis.com/css2?family=Source+Sans+3:wght@400;600&display=swap">
<style>
  :root {
    --backdrop: #5c4131;
    --paper: #f4f3f1;
    --ink: #4a4a4a;
    --ink-dark: #2b2b2b;
    --charcoal: #1c1d1d;
    --gold: #d4a42a;
    --gold-soft: #e3bd55;
    --rule: #c9c9c9;
  }
  * { box-sizing: border-box; margin: 0; padding: 0; }
  html, body { width: 1200px; height: 791px; overflow: hidden; }
  body {
    background: var(--backdrop);
    font-family: "Source Sans 3", "Myriad Pro", Arial, sans-serif;
    color: var(--ink);
    position: relative;
  }
  .sheet {
    position: absolute;
    background: var(--paper);
    overflow: hidden;
    box-shadow: 0 2px 6px rgba(0,0,0,.35);
  }
  .corner { position: absolute; width: 110px; height: 110px; }
  .corner--tl { left: 0; top: 0; }
  .corner--br { right: 0; bottom: 0; transform: rotate(180deg); }

  /* Letterhead */
  .letterhead { left: 38px; top: 34px; width: 513px; height: 723px; }
  .brand {
    position: absolute;
    font-weight: 600;
    color: var(--ink-dark);
    text-transform: uppercase;
    letter-spacing: .06em;
    white-space: nowrap;
  }
  .letterhead .brand { left: 40px; top: 78px; font-size: 15px; }
  .brand-rule { position: absolute; height: 1px; background: var(--gold); }
  .letterhead .brand-rule { left: 40px; top: 100px; width: 150px; }
  .contact {
    position: absolute;
    left: 340px; top: 38px;
    padding-left: 14px;
    border-left: 1px solid var(--rule);
    font-size: 7.6px;
    line-height: 9.6px;
    color: var(--ink);
    height: 68px;
  }
  .contact .company { color: var(--gold); }
  .contact .lines { margin-top: 0; }
  .contact ul { list-style: none; margin-top: 5px; }
  .contact li { display: flex; align-items: center; gap: 4px; margin-bottom: 2px; }
  .contact svg { width: 7px; height: 7px; flex: none; }

  .letter { position: absolute; left: 46px; top: 204px; width: 424px; }
  .salutation { font-size: 14px; color: var(--ink); margin-bottom: 25px; }
  .letter p.body {
    font-size: 7.9px;
    line-height: 12.6px;
    text-align: justify;
    margin-bottom: 12.6px;
    color: var(--ink);
  }
  .closing { font-size: 8px; margin-top: 26px; }
  .signature-mark {
    width: 72px; height: 24px; margin: 8px 0 6px -2px;
    background: linear-gradient(90deg, rgba(28,29,29,.15), rgba(28,29,29,.35), rgba(28,29,29,.1));
    border-radius: 12px;
  }
  .signer { font-size: 8.2px; line-height: 10px; padding-left: 3px; }

  /* Envelope back */
  .envelope-back { left: 577px; top: 216px; width: 576px; height: 261px; }
  .flap { position: absolute; left: 0; top: 0; width: 576px; height: 96px; }
  .flap-content {
    position: absolute; left: 0; top: 34px; width: 576px; text-align: center;
  }
  .flap-content .brand { position: static; color: var(--gold); font-size: 11px; }
  .flap-content .site { color: #fff; font-size: 8.5px; margin-top: 6px; }

  /* Envelope front */
  .envelope-front { left: 577px; top: 494px; width: 577px; height: 263px; }
  .envelope-front .brand { left: 31px; top: 58px; font-size: 13.5px; }
  .envelope-front .brand-rule { left: 31px; top: 76px; width: 145px; }
  .return-address {
    position: absolute; left: 31px; top: 88px;
    font-size: 7.8px; line-height: 9.6px; color: var(--ink);
  }
  .return-address .company { color: var(--gold); }
</style>
</head>
<body>

<section class="sheet letterhead" aria-label="Letterhead">
  <svg class="corner corner--tl" viewBox="0 0 110 110" aria-hidden="true">
    <path d="M0 0 H84 Q24 18 0 72 Z" fill="var(--charcoal)"/>
    <path d="M86 0 Q24 20 2 76" fill="none" stroke="var(--gold)" stroke-width="2.5"/>
  </svg>
  <svg class="corner corner--br" viewBox="0 0 110 110" aria-hidden="true">
    <path d="M0 0 H84 Q24 18 0 72 Z" fill="var(--charcoal)"/>
    <path d="M86 0 Q24 20 2 76" fill="none" stroke="var(--gold)" stroke-width="2.5"/>
  </svg>

  <div class="brand">Copperfen Holdings Inc</div>
  <div class="brand-rule"></div>

  <address class="contact" style="font-style:normal">
    <div class="company">Copperfen Holdings, Inc.</div>
    <div class="lines">48 Alder Row; Suite 210<br>Fenwick, IA 50999</div>
    <ul>
      <li><svg viewBox="0 0 10 10"><path d="M2 1 L4 1 L5 3 L4 4 Q5 6 6 6 L7 5 L9 6 L9 8 Q8 9 6 9 Q1 7 1 2 Z" fill="var(--gold)"/></svg>555-014-2280</li>
      <li><svg viewBox="0 0 10 10"><rect x="1" y="2" width="8" height="6" fill="var(--gold)"/><path d="M1 2 L5 5.5 L9 2" fill="none" stroke="var(--paper)" stroke-width="1"/></svg>inquiries@copperfenholdings.com</li>
      <li><svg viewBox="0 0 10 10"><circle cx="5" cy="5" r="4" fill="var(--gold)"/><path d="M1 5 H9 M5 1 Q2.5 5 5 9 M5 1 Q7.5 5 5 9" fill="none" stroke="var(--paper)" stroke-width=".7"/></svg>www.copperfenholdings.com</li>
    </ul>
  </address>

  <article class="letter">
    <h1 class="salutation" style="font-weight:400">Dear Mr. Marsh,</h1>
    <p class="body">Lorem ipsum dolor sit amet, consectetur adipiscing elit. Donec orci purus, luctus vitae dignissim eu, iaculis sed purus. Vivamus faucibus, ipsum nec aliquet viverra, leo mauris condimentum ligula, sit amet sagittis enim ligula quis arcu. Nam egestas tortor id nisi porttitor mattis. In tortor ante, ultricies in suscipit a, tempus non massa. Vivamus et auctor mi. Fusce vel massa nulla. Phasellus nec eros mauris, et scelerisque orci.</p>
    <p class="body">Donec malesuada orci vitae nulla accumsan porta a id massa. Quisque accumsan iaculis magna sit amet fringilla. Maecenas consequat, magna eget tincidunt semper, odio nibh rutrum mi, id feugiat ante nisi eu risus. Vestibulum nunc orci, rhoncus a placerat in, ultricies in mi. Cras mattis varius eros, vel fringilla nisi suscipit eget. Quisque scelerisque sagittis nulla at porttitor.</p>
    <p class="body">Sed id augue vitae urna euismod commodo aliquet a quam. Pellentesque arcu velit, cursus et malesuada ut, consequat et diam. Nullam erat sem, rhoncus id ullamcorper vitae, rhoncus et arcu. In ultricies ultricies nulla, ut rutrum nisi iaculis at. Donec eu magna a metus ornare faucibus. Fusce aliquet faucibus ultricies. Morbi semper, est id tincidunt gravida, sem arcu adipiscing lacus, ac bibendum nulla leo eu purus. Quisque nec diam sed risus consectetur a ccumsan quis quis nibh. Vestibulum id purus lorem.</p>
    <p class="body">It is a long established fact that a reader will be distracted by the readable content of a page when looking at its layout. The point of using Lorem Ipsum is that it has a more-or-less normal distribution of letters, as opposed to using 'Content here, content here', making it look like readable English. Many desktop publishing packages</p>
    <p class="closing">Sincerely,</p>
    <div class="signature-mark" role="img" aria-label="Handwritten signature"></div>
    <p class="signer">Alan Marsh<br>Founder</p>
  </article>
</section>

<section class="sheet envelope-back" aria-label="Envelope back">
  <svg class="flap" viewBox="0 0 576 96" aria-hidden="true">
    <path d="M0 0 H576 L562 12 L562 74 Q562 96 540 96 H36 Q14 96 14 74 L14 12 Z" fill="var(--charcoal)"/>
  </svg>
  <div class="flap-content">
    <div class="brand">Copperfen</div>
    <div class="site">www.copperfenholdings.com</div>
  </div>
</section>

<section class="sheet envelope-front" aria-label="Envelope front">
  <svg class="corner corner--tl" viewBox="0 0 110 110" aria-hidden="true" style="width:70px;height:70px">
    <path d="M0 0 H84 Q24 18 0 72 Z" fill="var(--charcoal)"/>
    <path d="M86 0 Q24 20 2 76" fill="none" stroke="var(--gold)" stroke-width="2.5"/>
  </svg>
  <svg class="corner corner--br" viewBox="0 0 110 110" aria-hidden="true" style="width:70px;height:70px">
    <path d="M0 0 H84 Q24 18 0 72 Z" fill="var(--charcoal)"/>
    <path d="M86 0 Q24 20 2 76" fill="none" stroke="var(--gold)" stroke-width="2.5"/>
  </svg>
  <div class="brand">Copperfen Holdings Inc</div>
  <div class="brand-rule"></div>
  <address class="return-address" style="font-style:normal">
    <div class="company">Copperfen Holdings, Inc.</div>
    48 Alder Row; Suite 210<br>Fenwick, IA 50999
  </address>
</section>

</body>
</html>
```